Marlow Creek Stud website

We would like to create a horse stud/agistment farm website similar to this websites we have attached below:
www.hollistead.com.au
www.quandrell.com.au
www.barrowick.com
www.fenshaw.com.au
The main colour scheme are purple and white to align with the stable's racing colours.
We have also attach the company logo and also images of the farm and create some ideas for the website.
Many thanks for looking into this project!

```html
<!DOCTYPE html>
<html lang="en">
<head>
<meta charset="utf-8">
<title>Marlow Creek Stud</title>
<link rel="stylesheet" href="https://fonts.googleapis.com/css2?family=Source+Sans+3:wght@300;400;600;700&family=Montserrat:wght@600;700&display=swap">
<style>
:root{
  --purple:#3f1a47;
  --purple-soft:#6b3c73;
  --accent:#e0261f;
  --white:#ffffff;
  --ink:#333333;
  --grey:#777777;
  --gold:#e8c21a;
  --dot:#3f1a47;
}
*{box-sizing:border-box;margin:0;padding:0}
html,body{width:1200px;height:1200px;overflow:hidden;background:var(--white)}
body{font-family:"Source Sans 3",sans-serif;color:var(--ink);position:relative}
.page{position:absolute;left:322.4px;top:0;width:696px;height:1500px;transform:scale(.8);transform-origin:0 0;background:var(--white);overflow:hidden}
.abs{position:absolute}
.center{text-align:center}

/* header */
.site-header{left:0;top:0;width:696px;height:65px;background:var(--purple)}
.brand{left:80px;top:22px;display:flex;align-items:center;gap:6px;color:var(--white);font-weight:600;font-size:12px}
.brand-dot{width:12px;height:12px;border:2px solid var(--white);border-radius:50%}
.nav a{position:absolute;top:11px;color:var(--white);text-decoration:none;font-weight:700;font-size:10px;letter-spacing:.2px}
.social{display:flex;gap:10px}
.social span{width:15px;height:15px;border-radius:50%;background:var(--white);display:block}
.header-social{left:517px;top:37px}

/* hero */
.hero{left:0;top:65px;width:696px;height:295px;background:linear-gradient(180deg,#8d94a0 0%,#a4a39a 22%,#6f7f52 45%,#4f7a2c 70%,#355a1d 100%)}
.hero-title{left:0;top:85px;width:696px;font-weight:700;font-size:24px;color:var(--white);text-shadow:0 1px 3px rgba(0,0,0,.6);letter-spacing:.3px}
.hero-sub{left:0;top:170px;width:696px;font-size:15px;color:var(--white);text-shadow:0 1px 3px rgba(0,0,0,.6)}
.hero-body{left:0;top:289px;width:696px;font-size:9.5px;font-weight:700;line-height:15.5px;color:var(--white);text-shadow:0 1px 2px rgba(0,0,0,.8)}

/* features */
.section-title{left:0;top:376px;width:696px;font-weight:700;font-size:17px;color:var(--purple)}
.section-sub{left:0;top:397px;width:696px;font-size:7.5px;color:var(--purple-soft)}
.feature{top:424px;width:120px;text-align:center}
.feature svg{display:block;margin:0 auto;height:64px}
.feature-label{font-size:8px;margin-top:6px;color:var(--ink)}
.feature-text{font-size:5.3px;line-height:10.8px;color:var(--grey);margin-top:6px;height:34px}
.btn-outline{display:inline-block;margin-top:10px;width:52px;height:21px;line-height:18px;border:1.5px solid var(--purple);border-radius:11px;color:var(--accent);font-size:5.5px;font-weight:600}

/* webcam band */
.webcam-band{left:0;top:602px;width:696px;height:37px;background:var(--purple)}
.webcam-text{left:123px;top:610px;font-family:"Montserrat",sans-serif;font-weight:600;font-size:12.5px;color:var(--white)}
.webcam-text em{font-style:normal;color:var(--accent)}
.btn-live{left:509px;top:607px;width:60px;height:27px;border:1.5px solid var(--white);border-radius:14px;color:var(--white);font-family:"Montserrat",sans-serif;font-weight:700;font-size:13px;line-height:24px;text-align:center}

/* gallery */
.photo{width:250px;height:167px}
.p1{left:87px;top:670px;background:linear-gradient(180deg,#6f9ed8 0%,#b7cbe2 45%,#4b3a2a 60%,#4d8a2c 85%)}
.p2{left:359px;top:670px;background:linear-gradient(180deg,#bfc1bf 0%,#7d8679 25%,#2d4a25 33%,#4d8a2c 60%,#3f7a22 100%)}
.p3{left:87px;top:858px;background:linear-gradient(180deg,#3c6fbe 0%,#9ab8d9 30%,#4f8a34 50%,#6f7a5a 75%,#3a6a22 100%)}
.p4{left:359px;top:858px;background:linear-gradient(180deg,#5d7fb6 0%,#9aaabf 10%,#3b6a2a 30%,#62a03a 65%,#4b8a2a 100%)}
.dots-v{left:347px;top:670px;width:0;height:358px;border-left:2px dotted var(--dot)}
.dots-h{left:87px;top:847px;width:525px;height:0;border-top:2px dotted var(--dot)}
.btn-see{left:318px;top:1044px;width:59px;height:17px;border-radius:9px;background:var(--purple);color:var(--white);font-size:5px;line-height:17px;text-align:center}
.rule{left:150px;top:1078px;width:395px;height:1.5px;background:var(--purple-soft)}

/* comments */
.comments-title{left:0;top:1092px;width:696px;font-weight:300;font-size:16px;color:var(--purple)}
.comments-sub{left:0;top:1115px;width:696px;font-size:7.5px;color:var(--ink)}
.arrow{top:1160px}
.review{top:1142px;width:110px;text-align:center}
.avatar{width:60px;height:60px;border-radius:50%;margin:0 auto;border:2px solid #eee;background:radial-gradient(circle at 50% 45%,#e6b9a0 0%,#c89478 45%,#f2f2f2 75%)}
.review-name{font-size:5.5px;font-weight:700;margin-top:7px}
.stars{color:var(--gold);font-size:11px;letter-spacing:-.5px;margin-top:2px;line-height:14px}
.review-text{font-size:5.3px;line-height:10px;color:var(--grey);margin-top:2px}

/* footer */
.footer{left:0;top:1300px;width:696px;height:200px;border-top:2px solid var(--purple);background:linear-gradient(180deg,#6b6a66 0%,#3a3a2c 25%,#2f3a1f 50%,#3f6a24 75%,#4f8a2c 100%)}
.btn-details{left:277px;top:1285px;width:142px;height:31px;border-radius:16px;background:var(--purple);color:var(--white);font-size:6.5px;line-height:31px;text-align:center}
.f-col{top:1343px;color:var(--white);font-size:6px}
.f-col h4{font-weight:400;font-size:6.5px;margin-bottom:9px}
.f-col li{list-style:none;line-height:17.3px}
.f-address li{line-height:11.3px;color:#ddd}
.newsletter p{line-height:11.5px;width:130px}
.nl-input{width:132px;height:16px;background:var(--white);margin-top:5px;color:#999;font-size:4.5px;line-height:16px;padding-left:7px}
.nl-submit{width:40px;height:16px;border-radius:8px;background:var(--purple);margin-top:10px;font-size:4.8px;line-height:16px;text-align:center}
.footer-social{left:293px;top:1463px}
.footer-social span{width:14px;height:14px}
.copyright{left:0;top:1487px;width:696px;font-size:4.5px;color:var(--white)}
</style>
</head>
<body>
<main class="page">

  <header class="site-header abs">
    <div class="brand abs"><span class="brand-dot"></span>Marlow Creek Stud</div>
    <nav class="nav">
      <a style="left:312px">HOME</a>
      <a style="left:373px">FARM</a>
      <a style="left:432px">NEWS</a>
      <a style="left:492px">GALLERY</a>
      <a style="left:566px">CONTACT</a>
    </nav>
    <div class="social header-social abs"><span></span><span></span><span></span><span></span></div>
  </header>

  <section class="hero abs" role="img" aria-label="Photo of green paddocks with timber fences and a grazing horse at sunset"></section>
  <h1 class="hero-title abs center">MARLOW CREEK STUD - A PLACE WHERE TO BE</h1>
  <p class="hero-sub abs center">We trust our ideas to make them alive</p>
  <p class="hero-body abs center">Lorem ipsum dolor sit amet, consectetur adipisicing elit,<br>sed do eiusmod tempor incididunt ut labore et dolore magna aliqua.<br>Ut enim ad minim veniam, quis nostrud exercitation ullamco laboris nisi ut aliquip.</p>

  <h2 class="section-title abs center">Our best to make everything the best</h2>
  <p class="section-sub abs center">Protect your ebooks wihtout spending a fortune on complicated software</p>

  <div class="feature abs" style="left:92px">
    <svg viewBox="0 0 64 64" aria-hidden="true"><g fill="var(--purple)">
      <polygon points="6,8 10,0 14,8 14,64 6,64"/><polygon points="20,8 24,0 28,8 28,64 20,64"/>
      <polygon points="34,8 38,0 42,8 42,64 34,64"/><polygon points="48,8 52,0 56,8 56,64 48,64"/>
      <rect x="0" y="20" width="64" height="7"/><rect x="0" y="42" width="64" height="7"/></g></svg>
    <div class="feature-label">Well organized</div>
    <div class="feature-text">Pellentesque consequat viverra diam at viverra. Vivamus ac blandit elit, id molestie sem. Suspendisse malesuada id nisl vitae feugiat...</div>
    <span class="btn-outline">LEARN MORE</span>
  </div>
  <div class="feature abs" style="left:223px">
    <svg viewBox="0 0 64 64" aria-hidden="true"><g fill="none" stroke="var(--purple)" stroke-width="1.5">
      <polygon points="2,1 62,1 46,24 18,24"/><polygon points="10,1 54,1 40,20 24,20"/>
      <circle cx="32" cy="44" r="18"/><circle cx="32" cy="44" r="13"/></g>
      <circle cx="32" cy="44" r="4" fill="var(--purple)"/></svg>
    <div class="feature-label">Our awards</div>
    <div class="feature-text">Donec hendrerit neque neque, eget consectetur diam tincidunt ut. Nulla ut lobortis justo. Etiam id lacinia libero.</div>
    <span class="btn-outline">LEARN MORE</span>
  </div>
  <div class="feature abs" style="left:353px">
    <svg viewBox="0 0 64 64" aria-hidden="true">
      <path d="M22 28 V16 a10 10 0 0 1 20 0 V20" fill="none" stroke="var(--purple)" stroke-width="5"/>
      <rect x="12" y="28" width="40" height="36" rx="3" fill="var(--purple)"/>
      <circle cx="32" cy="43" r="5" fill="var(--white)"/><rect x="30" y="44" width="4" height="9" fill="var(--white)"/></svg>
    <div class="feature-label">Safe zone</div>
    <div class="feature-text">bibendum egestas. Donec aliquam nulla dolor, in eleifend diam molestie sed. Phasellus nec fringilla sem.</div>
    <span class="btn-outline">LEARN MORE</span>
  </div>
  <div class="feature abs" style="left:483px">
    <svg viewBox="0 0 70 64" aria-hidden="true"><g fill="var(--purple)">
      <circle cx="35" cy="8" r="7"/><circle cx="16" cy="16" r="7"/><circle cx="54" cy="16" r="7"/>
      <rect x="24" y="17" width="22" height="24" rx="3"/><rect x="2" y="27" width="28" height="37" rx="3"/><rect x="40" y="27" width="28" height="37" rx="3"/></g></svg>
    <div class="feature-label">Friendly environment</div>
    <div class="feature-text">Aliquam tincidunt non nisi id faucibus. Vestibulum eget diam id justo rhoncus luctus. Nullam pretium ut turpis non commodo.</div>
    <span class="btn-outline">LEARN MORE</span>
  </div>

  <div class="webcam-band abs"></div>
  <p class="webcam-text abs">To <em>see</em> what we are doing every day, check our webcams</p>
  <div class="btn-live abs">LIVE</div>

  <div class="photo p1 abs" role="img" aria-label="Photo of five young horses standing in a paddock under a blue sky"></div>
  <div class="photo p2 abs" role="img" aria-label="Photo of a pale horse grazing in a green field"></div>
  <div class="photo p3 abs" role="img" aria-label="Aerial photo of the stud buildings and surrounding paddocks"></div>
  <div class="photo p4 abs" role="img" aria-label="Aerial photo of fenced paddocks with small shelters"></div>
  <div class="dots-v abs"></div>
  <div class="dots-h abs"></div>
  <div class="btn-see abs">SEE MORE</div>
  <div class="rule abs"></div>

  <h2 class="comments-title abs center">Last comments who can help you</h2>
  <p class="comments-sub abs center">Vivamus eleifend, nunc at vehicula mollis, mauris libero imperdiet</p>
  <svg class="arrow abs" style="left:96px" width="14" height="26" viewBox="0 0 14 26" aria-hidden="true"><polyline points="12,2 2,13 12,24" fill="none" stroke="#888" stroke-width="2.5"/></svg>
  <svg class="arrow abs" style="left:586px" width="14" height="26" viewBox="0 0 14 26" aria-hidden="true"><polyline points="2,2 12,13 2,24" fill="none" stroke="#888" stroke-width="2.5"/></svg>

  <div class="review abs" style="left:112px">
    <div class="avatar" role="img" aria-label="Portrait photo of Odile Varran"></div>
    <div class="review-name">Odile VARRAN</div><div class="stars">★★★★★</div>
    <div class="review-text">Nunc ultricies vel augue ac<br>elementum. Donec hendrerit<br>[...]</div>
  </div>
  <div class="review abs" style="left:234px">
    <div class="avatar" role="img" aria-label="Portrait photo of Bastien Corlay"></div>
    <div class="review-name">Bastien CORLAY</div><div class="stars">★★★★★</div>
    <div class="review-text">Fusce at pharetra diam.<br>Suspendisse id quam volutpat sem<br>[...]</div>
  </div>
  <div class="review abs" style="left:357px">
    <div class="avatar" role="img" aria-label="Portrait photo of Glen Hartwick"></div>
    <div class="review-name">Glen HARTWICK</div><div class="stars">★★★★★</div>
    <div class="review-text">Proin fermentum, felis ut pharetra<br>iaculis, lacus ligula posuere<br>[...]</div>
  </div>
  <div class="review abs" style="left:479px">
    <div class="avatar" role="img" aria-label="Portrait photo of Tessa Moreau"></div>
    <div class="review-name">Tessa MOREAU</div><div class="stars">★★★★★</div>
    <div class="review-text">Sed consequat mi sit amet<br>posuere tempor. In id interdum<br>[...]</div>
  </div>

  <footer class="footer abs" role="img" aria-label="Photo of green hillside paddocks with trees and grazing horses"></footer>
  <div class="btn-details abs">FOR MORE DETAILS</div>

  <div class="f-col abs" style="left:109px"><h4>TEAM</h4><ul><li>Rowan</li><li>Celia</li><li>Dario</li><li>Finn</li></ul></div>
  <div class="f-col abs" style="left:175px"><h4>ABOUT US</h4><ul><li>Where</li><li>From</li><li>Why</li></ul></div>
  <div class="f-col abs" style="left:251px"><h4>SUPPORT</h4><ul><li>Links</li><li>Call us</li><li>Email us</li><li>Policy</li><li>Insurrance</li></ul></div>
  <div class="f-col f-address abs" style="left:326px"><h4>ADDRESS</h4><ul><li>Marlow Creek Stud</li><li>XXX</li><li>XXXXXXXX</li><li>XXXXXXXXXX</li><li>Phone: +61 455 218 730</li></ul></div>
  <div class="f-col newsletter abs" style="left:454px"><h4>OUR NEWSLETTER IS ON</h4>
    <p>Get our last notice for free and stay tune to any update and projects</p>
    <div class="nl-input">Here type your email address</div>
    <div class="nl-submit">SUBMIT</div>
  </div>

  <div class="social footer-social abs"><span></span><span></span><span></span><span></span></div>
  <p class="copyright abs center">Copyright © 2015 &nbsp; All Rights Reserved to Marlow Creek Stud</p>

</main>
</body>
</html>
```